new signage design for budget motel - Brookfern Lodge

renaming the budget motel as Brookfern Lodge, property located on side of a hill. therefore i choose to name is Brookfern Lodge, im looking for clean, modern look in signage design,this property does not have a Logo, plan to us signage design as a logo as well. current pole sign housing is rectangle shape and will be using same housing I'll be attaching picture of the signage for better idea. looking forward to awesome creative designs.

Industry/Entity Type

Motel

Font styles to use
Serif
Sans Serif

Requirements
Should not have
• mountains , mountain(s) with snow , trees, no black color, red color, blue letters, too much green.

```html
<!DOCTYPE html>
<html lang="en">
<head>
<meta charset="UTF-8">
<title>Brookfern Lodge – Pole Sign</title>
<link href="https://fonts.googleapis.com/css2?family=Montserrat:wght@700;800&display=swap" rel="stylesheet">
<style>
  :root {
    --canvas-bg: #eceeea;
    --sign-white: #ffffff;
    --sunny-yellow: #ffcc00;
    --leaf-green: #9ecb3a;
    --text-white: #ffffff;
  }
  html, body {
    margin: 0;
    padding: 0;
    width: 1200px;
    height: 900px;
    overflow: hidden;
    background: var(--canvas-bg);
  }
  .canvas {
    position: relative;
    width: 1200px;
    height: 900px;
  }
  .sign-panel {
    position: absolute;
    left: 40px;
    top: 135px;
    width: 1120px;
    height: 630px;
    background: var(--sign-white);
    overflow: hidden;
    box-shadow: 0 6px 24px rgba(60, 70, 50, 0.12);
  }
  .sign-shapes {
    position: absolute;
    inset: 0;
  }
  .tagline {
    position: absolute;
    left: 0;
    right: 0;
    top: 72px;
    margin: 0;
    text-align: center;
    font-family: 'Montserrat', sans-serif;
    font-weight: 800;
    font-size: 30px;
    line-height: 1.12;
    letter-spacing: 0.5px;
    color: var(--sunny-yellow);
    text-transform: uppercase;
  }
  .tagline-first {
    display: inline-flex;
    align-items: center;
    gap: 14px;
  }
  .tagline-rule {
    display: inline-block;
    width: 64px;
    height: 4px;
    background: var(--leaf-green);
  }
  .brand-name {
    position: absolute;
    left: 0;
    right: 0;
    top: 172px;
    margin: 0;
    text-align: center;
    font-family: 'Montserrat', sans-serif;
    font-weight: 800;
    font-size: 118px;
    line-height: 1.0;
    letter-spacing: -1px;
    color: var(--leaf-green);
  }
  .call-band {
    position: absolute;
    left: 95px;
    top: 480px;
    width: 890px;
    height: 118px;
    background: var(--leaf-green);
    display: flex;
    align-items: center;
    padding-left: 40px;
    box-sizing: border-box;
  }
  .call-text {
    margin: 0;
    font-family: 'Montserrat', sans-serif;
    font-weight: 800;
    font-size: 74px;
    letter-spacing: 1px;
    color: var(--text-white);
  }
</style>
</head>
<body>
  <main class="canvas">
    <section class="sign-panel" aria-label="Brookfern Lodge pole sign">
      <svg class="sign-shapes" width="1120" height="630" viewBox="0 0 1120 630" aria-hidden="true">
        <!-- top-right corner triangle -->
        <path class="corner-triangle" d="M800 0 H1120 V300 Q1110 345 1060 310 L830 70 Q800 35 800 0 Z" fill="var(--sunny-yellow)"/>
        <rect class="corner-diamond" x="0" y="0" width="92" height="92" rx="10" transform="translate(880 -22) rotate(45)" fill="var(--leaf-green)"/>
        <!-- left edge triangle -->
        <path class="edge-triangle" d="M0 220 L110 340 Q130 365 110 390 L0 530 Z" fill="var(--sunny-yellow)"/>
        <rect class="edge-diamond" x="0" y="0" width="56" height="56" rx="6" transform="translate(64 420) rotate(45)" fill="var(--leaf-green)"/>
      </svg>

      <p class="tagline">
        <span class="tagline-first"><span class="tagline-rule"></span>Property that<span class="tagline-rule"></span></span><br>
        Located on side of a hill
      </p>

      <h1 class="brand-name">Brookfern<br>Lodge</h1>

      <div class="call-band">
        <p class="call-text">CALL 000000000</p>
      </div>
    </section>
  </main>
</body>
</html>
```